Billboard design for agricultural machinery business

hello im looking for roadside advertiement sign to be designed, the sign is 10ft up in the air and is 4ft high and 8ft wide, id image i like a blue background and my logo front and centre and below logo sales - service - parts and then below that the ferro vale symbol and brisk symbol, I’d also like the website www.Ploverbay.ie on it. i am open to suggestions and designs. blue is #005999 and yellow is rgb (254, 205, 26) ive attached my log and symbols, im open to different colour backgrounds or just white and also open to ferro vale and brisk as writhing rather than logos

Target Market(s)

Ferro Vale and brisk tractor owners

Industry/Entity Type

Agricultural machine sales service and parts

Colors

Designer to choose colors to be used in the design.

Requirements
Must have
• My logo and colours, brands ferro Vale and brisk, website

```html
<!DOCTYPE html>
<html lang="en">
<head>
<meta charset="utf-8">
<title>Ploverbay Billboard</title>
<link rel="stylesheet" href="https://fonts.googleapis.com/css2?family=Rubik:wght@600;700;800&display=swap">
<style>
  :root {
    --brand-blue: #005999;
    --deep-blue: #0b4f92;
    --brand-yellow: rgb(254, 205, 26);
    --accent-red: #b1202c;
    --white: #ffffff;
  }
  * { box-sizing: border-box; margin: 0; padding: 0; }
  html, body { width: 1200px; height: 730px; overflow: hidden; background: #e9edf1; }
  .billboard {
    position: relative;
    width: 1200px;
    height: 730px;
    background: var(--brand-blue);
    overflow: hidden;
    font-family: "Rubik", sans-serif;
    color: var(--white);
  }
  .waves { position: absolute; inset: 0; }
  .brand-mark {
    position: absolute;
    top: 130px;
    left: 0;
    width: 1200px;
    display: flex;
    justify-content: center;
    align-items: center;
    gap: 22px;
  }
  .brand-mark__dot {
    flex-shrink: 0;
    width: 56px; height: 56px;
    border-radius: 50%;
    background: var(--brand-yellow);
  }
  .brand-mark__name {
    font-size: 128px;
    font-weight: 800;
    letter-spacing: -1px;
    color: var(--white);
    line-height: 1;
  }
  .tagline {
    position: absolute;
    top: 320px;
    left: 0;
    width: 1200px;
    text-align: center;
    font-size: 64px;
    font-weight: 700;
    letter-spacing: 0.5px;
    line-height: 1.1;
  }
  .tagline .sep { color: var(--brand-yellow); margin: 0 18px; }
  .partners {
    position: absolute;
    top: 492px;
    left: 60px;
    display: flex;
    align-items: center;
    gap: 22px;
    font-weight: 700;
    font-size: 32px;
    line-height: 1;
  }
  .partners__divider { width: 2px; height: 56px; background: var(--white); opacity: .8; }
  .contact {
    position: absolute;
    right: 80px;
    top: 522px;
    text-align: right;
    color: var(--deep-blue);
    font-weight: 700;
  }
  .contact__phone { font-size: 62px; line-height: 1; }
  .contact__web { font-size: 36px; line-height: 1.1; margin-top: 10px; }
  .social {
    position: absolute;
    left: 110px;
    top: 674px;
    display: flex;
    align-items: center;
    gap: 28px;
    color: var(--deep-blue);
    font-size: 18px;
    font-weight: 700;
    line-height: 1;
  }
  .social__item { display: flex; align-items: center; gap: 10px; white-space: nowrap; }
  .social__dot {
    flex-shrink: 0;
    width: 34px; height: 34px; border-radius: 50%;
    background: var(--deep-blue);
    border: 3px solid var(--white);
  }
</style>
</head>
<body>
<main class="billboard">
  <svg class="waves" viewBox="0 0 1200 730" width="1200" height="730" aria-hidden="true">
    <path d="M600 486 C 800 410, 1000 385, 1200 378 L1200 450 C 1040 440, 860 450, 600 486 Z" fill="var(--accent-red)"/>
    <path d="M560 520 C 760 450, 980 425, 1200 440" fill="none" stroke="var(--deep-blue)" stroke-width="10"/>
    <path d="M0 640 C 260 690, 480 600, 680 505 C 860 430, 1060 428, 1200 446 L1200 730 L0 730 Z" fill="var(--brand-yellow)"/>
    <path d="M0 640 C 260 690, 480 600, 680 505 C 860 430, 1060 428, 1200 446" fill="none" stroke="var(--white)" stroke-width="8"/>
  </svg>

  <div class="brand-mark">
    <span class="brand-mark__dot"></span>
    <span class="brand-mark__name">Ploverbay</span>
  </div>

  <p class="tagline">Sales<span class="sep">•</span>Service<span class="sep">•</span>Parts</p>

  <div class="partners">
    <span class="partners__name">BRISK</span>
    <span class="partners__divider"></span>
    <span class="partners__name">FERRO VALE</span>
  </div>

  <div class="contact">
    <p class="contact__phone">085 555 0142</p>
    <p class="contact__web">www.ploverbay.ie</p>
  </div>

  <div class="social">
    <span class="social__item"><span class="social__dot"></span>Chatter</span>
    <span class="social__item"><span class="social__dot"></span>Clipline</span>
  </div>
</main>
</body>
</html>
```